Design a styled business card for an intimacy and attachment psychologist

I am a Psychologist providing online therapy to patients across the United States. My work is interpersonal and emotion-focused, with an emphasis on the client-therapist relationship. My primary areas of work are very personal, including sexuality and gender, abuse and trauma, and grief and loss. My target audience will be adults of all ages 18+.
My business card should convey a warm and inviting feeling of professionalism that is also casual and comfortable.
The front should be fairly simple and professional, consisting of:
- My name, Dr. Rosalind Petrakis
- My title, Licensed Psycholigist
- My logo
On either the front or the back, my contact information should be listed:
- ros@drrospetrakis.example
- 555.014.7788
- drrospetrakis.example
On the rear, I would like a description of the areas that I specialize in. This can be formatted in any way that appears stylistically interesting.
Individual and Couples
Relationships and Infidelity
Sexual Health & Aging
Gender Identity & Sexual Orientation
Abuse and Trauma
Sexual Compulsivity & Addiction
Sexual Dysfunction
Target Market(s)
My target audience will be adults of all ages 18+.
Industry/Entity Type
Psychology
Contact Information for Business Card
The front should be fairly simple and professional, consisting of: - My name, Dr. Rosalind Petrakis - My title, Licensed Psycholigist - My logo On either the front or the back, my contact information should be listed: - ros@drrospetrakis.example - 555.014.7788 - drrospetrakis.example On the rear, I would like a description of the areas that I specialize in. This can be formatted in any way that appears stylistically interesting. Individual and Couples Relationships and Infidelity Sexual Health & Aging Gender Identity & Sexual Orientation Abuse and Trauma Sexual Compulsivity & Addiction Sexual Dysfunction
- Follow brand guide

```html
<!DOCTYPE html>
<html lang="en">
<head>
<meta charset="utf-8">
<title>Dr. Rosalind Petrakis — Business Card</title>
<link rel="stylesheet" href="https://fonts.googleapis.com/css2?family=Montserrat:wght@400;500;700&display=swap">
<style>
  :root {
    --stage: #2b2b2d;
    --teal: #62c4ab;
    --teal-light: #cfe9e1;
    --navy: #2a2347;
    --red: #ef3e3e;
    --orange: #f6a623;
    --purple: #9b55a8;
    --white: #ffffff;
    --ink: #1e1e24;
  }
  * { box-sizing: border-box; margin: 0; padding: 0; }
  html, body { width: 1200px; height: 689px; overflow: hidden; }
  body {
    background: var(--stage);
    font-family: "Montserrat", sans-serif;
    position: relative;
  }
  .card {
    position: absolute;
    top: 181px;
    width: 570px;
    height: 326px;
    overflow: hidden;
  }
  /* ---------- Back ---------- */
  .card-back { left: 20px; background: var(--teal); }
  .back-mark {
    position: absolute;
    left: 40px; top: 63px;
    width: 200px; height: 200px;
    border-radius: 50%;
    border: 8px solid var(--navy);
    background: var(--teal-light);
    display: flex; align-items: center; justify-content: center;
    text-align: center;
    color: var(--navy);
    font-weight: 700;
    font-size: 19px;
    line-height: 1.2;
    padding: 20px;
  }
  .back-divider { position: absolute; left: 262px; top: 40px; }
  .back-faint {
    position: absolute;
    right: -40px; top: -30px;
    width: 240px; height: 240px;
    border-radius: 50%;
    border: 10px solid rgba(255,255,255,0.12);
  }
  .specialties {
    position: absolute;
    left: 310px; top: 52px;
    list-style: none;
    color: var(--white);
    font-size: 13.5px;
    font-weight: 500;
  }
  .specialties li {
    display: flex; align-items: flex-start;
    gap: 8px;
    line-height: 1.2;
    margin-bottom: 9px;
  }
  .specialties svg { flex: none; margin-top: 1px; }
  /* ---------- Front ---------- */
  .card-front { left: 610px; background: var(--white); }
  .name-accent {
    position: absolute; left: 0; top: 86px;
    width: 14px; height: 46px;
    background: var(--teal);
  }
  .name {
    position: absolute; left: 30px; top: 86px;
    font-size: 22px; font-weight: 700;
    letter-spacing: 0.5px;
    color: var(--red);
  }
  .name .surname { color: var(--teal); }
  .title {
    position: absolute; left: 30px; top: 114px;
    font-size: 13px; color: var(--ink);
  }
  .brand {
    position: absolute; right: 30px; top: 46px;
    display: flex; align-items: center; gap: 12px;
  }
  .brand-dot {
    width: 60px; height: 60px; border-radius: 50%;
    background: var(--teal);
  }
  .brand-name {
    font-size: 17px; font-weight: 700;
    color: var(--navy);
    line-height: 1.15;
  }
  .contact {
    position: absolute; left: 30px; top: 190px;
    list-style: none;
    font-size: 13px; color: var(--ink);
  }
  .contact li { display: flex; align-items: center; gap: 10px; margin-bottom: 7px; }
  .band { position: absolute; left: 0; bottom: 0; }
</style>
</head>
<body>

<section class="card card-back" aria-label="Card back: areas of practice">
  <div class="back-faint" aria-hidden="true"></div>
  <div class="back-mark">Dr. Rosalind Petrakis</div>
  <svg class="back-divider" width="40" height="250" viewBox="0 0 40 250" aria-hidden="true">
    <line x1="4" y1="10" x2="30" y2="240" stroke="var(--orange)" stroke-width="1.5"/>
    <line x1="10" y1="20" x2="34" y2="230" stroke="var(--orange)" stroke-width="1.5"/>
    <line x1="16" y1="30" x2="38" y2="220" stroke="var(--orange)" stroke-width="1.5"/>
  </svg>
  <ul class="specialties">
    <li><svg width="15" height="15" viewBox="0 0 16 16"><circle cx="8" cy="8" r="6.5" fill="none" stroke="var(--orange)" stroke-width="2"/><path d="M4.5 8l2.5 2.5L12 5" fill="none" stroke="var(--orange)" stroke-width="2"/></svg>Individual and Couples</li>
    <li><svg width="15" height="15" viewBox="0 0 16 16"><circle cx="8" cy="8" r="6.5" fill="none" stroke="var(--orange)" stroke-width="2"/><path d="M4.5 8l2.5 2.5L12 5" fill="none" stroke="var(--orange)" stroke-width="2"/></svg>Relationships and Infidelity</li>
    <li><svg width="15" height="15" viewBox="0 0 16 16"><circle cx="8" cy="8" r="6.5" fill="none" stroke="var(--orange)" stroke-width="2"/><path d="M4.5 8l2.5 2.5L12 5" fill="none" stroke="var(--orange)" stroke-width="2"/></svg>Sexual Health &amp; Aging</li>
    <li><svg width="15" height="15" viewBox="0 0 16 16"><circle cx="8" cy="8" r="6.5" fill="none" stroke="var(--orange)" stroke-width="2"/><path d="M4.5 8l2.5 2.5L12 5" fill="none" stroke="var(--orange)" stroke-width="2"/></svg><span>Gender Identity &amp;<br>Sexual Orientation</span></li>
    <li><svg width="15" height="15" viewBox="0 0 16 16"><circle cx="8" cy="8" r="6.5" fill="none" stroke="var(--orange)" stroke-width="2"/><path d="M4.5 8l2.5 2.5L12 5" fill="none" stroke="var(--orange)" stroke-width="2"/></svg>Abuse and Trauma</li>
    <li><svg width="15" height="15" viewBox="0 0 16 16"><circle cx="8" cy="8" r="6.5" fill="none" stroke="var(--orange)" stroke-width="2"/><path d="M4.5 8l2.5 2.5L12 5" fill="none" stroke="var(--orange)" stroke-width="2"/></svg>Sexual Compulsivity &amp; Addiction</li>
    <li><svg width="15" height="15" viewBox="0 0 16 16"><circle cx="8" cy="8" r="6.5" fill="none" stroke="var(--orange)" stroke-width="2"/><path d="M4.5 8l2.5 2.5L12 5" fill="none" stroke="var(--orange)" stroke-width="2"/></svg>Sexual Dysfunction</li>
  </ul>
</section>

<section class="card card-front" aria-label="Card front: contact details">
  <div class="brand">
    <div class="brand-dot" aria-hidden="true"></div>
    <div class="brand-name">Dr. Rosalind<br>Petrakis</div>
  </div>
  <div class="name-accent" aria-hidden="true"></div>
  <h1 class="name">DR. ROSALIND <span class="surname">PETRAKIS</span></h1>
  <p class="title">Licensed Psycholigist</p>
  <ul class="contact">
    <li><svg width="14" height="14" viewBox="0 0 16 16" aria-hidden="true"><path d="M2 5c0-2 2-3 6-3s6 1 6 3l-3 1-1-2H6L5 6zM4 8h8l2 6H2z" fill="var(--red)"/></svg>555.014.7788</li>
    <li><svg width="14" height="14" viewBox="0 0 16 16" aria-hidden="true"><rect x="1" y="3" width="14" height="10" fill="var(--red)"/><path d="M1 3l7 6 7-6" fill="none" stroke="var(--white)" stroke-width="1.3"/></svg>ros@drrospetrakis.example</li>
    <li><svg width="14" height="14" viewBox="0 0 16 16" aria-hidden="true"><circle cx="8" cy="8" r="7" fill="var(--red)"/><path d="M1 8h14M8 1c-3 3-3 11 0 14M8 1c3 3 3 11 0 14" fill="none" stroke="var(--white)" stroke-width="1"/></svg>www.drrospetrakis.example</li>
  </ul>
  <svg class="band" width="570" height="90" viewBox="0 0 570 90" aria-hidden="true">
    <polygon points="0,90 0,72 420,72 440,30 570,30 570,90" fill="var(--teal)"/>
    <rect x="0" y="60" width="180" height="8" fill="var(--purple)"/>
    <rect x="184" y="52" width="150" height="8" fill="var(--red)"/>
    <rect x="338" y="44" width="90" height="8" fill="var(--orange)"/>
  </svg>
</section>

</body>
</html>
```